Marigold Works Flyer - RV Solar and Residential Solar

We would like to create a tri-fold brochure for our company for distribution in the mail. This will advertise our services, products and some references.

Our cover page should include a logo and contact information as well as some solar stock imagery.

Our inside pages should cover residential solar, RV solar and a solar education / facts portion.

The rear pages would be left for our remaining services and some references / testimonials.

Target Market(s)

Residential Homeowners and Recreational Vehicles

Industry/Entity Type

Solar Energy

Font styles to use
Serif
Sans Serif

Requirements
Must have
• Must match the color scheme of our logo.
Nice to have
• Solar stock images for RV solar and residential solar.
Either a black or white background with our logo is eye-catching,

```html
<!DOCTYPE html>
<html lang="en">
<head>
<meta charset="utf-8">
<title>Marigold Works Tri-fold Brochure</title>
<link href="https://fonts.googleapis.com/css2?family=Montserrat:ital,wght@0,300;0,400;0,500;0,600;0,700;0,800;1,600&display=swap" rel="stylesheet">
<style>
:root{
  --ink:#1b1d21;
  --ink-2:#26292f;
  --royal:#3446b4;
  --sky:#2fb3e8;
  --leaf:#5db33a;
  --paper:#ffffff;
  --mist:#e9ecf3;
  --stage:#c9c9cb;
  --grey-text:#4a4d55;
}
*{box-sizing:border-box;margin:0;padding:0}
html,body{width:1200px;height:2400px;overflow:hidden}
body{background:var(--stage);font-family:'Montserrat',sans-serif;color:var(--ink);position:relative}
.spread{position:absolute;left:40px;width:1120px;height:1080px;display:flex;box-shadow:0 14px 40px rgba(0,0,0,.25)}
.spread--outside{top:70px}
.spread--inside{top:1250px}
.panel{position:relative;width:373.33px;height:100%;overflow:hidden}
.photo{position:absolute;left:0;right:0}
.brand{font-weight:800;text-transform:uppercase;color:var(--royal);letter-spacing:1px;text-align:center;display:flex;align-items:center;justify-content:center;gap:10px;white-space:nowrap}
.brand .dot{width:14px;height:14px;border-radius:50%;background:var(--sky);flex:none}
.section-kicker{font-size:19px;font-weight:600;font-style:italic;color:var(--royal);text-transform:uppercase;line-height:1.1}
.section-title{font-size:21px;font-weight:800;text-transform:uppercase;line-height:1.1}
.rule{width:34px;height:4px;background:var(--royal);margin:10px 0 18px}
.list{list-style:none}
.list li{position:relative;padding-left:20px;font-size:12.5px;line-height:1.35;margin-bottom:9px}
.list li::before{content:"";position:absolute;left:2px;top:4px;width:8px;height:5px;border-left:2px solid var(--sky);border-bottom:2px solid var(--sky);transform:rotate(-45deg)}
.two-col{display:grid;grid-template-columns:1fr 1fr;column-gap:16px}
.dark{position:absolute;left:0;right:0;bottom:0;background:var(--ink)}
.swoosh{position:absolute;left:0;width:100%}
/* cover */
.cover-brand{position:absolute;top:120px;left:0;right:0;font-size:27px}
.cover-headline{position:absolute;left:34px;right:20px;top:770px;color:var(--paper);text-transform:uppercase;font-size:29px;line-height:1.12;font-weight:400;letter-spacing:1px}
.cover-headline .green{color:var(--leaf);font-weight:800;font-size:38px}
.cover-headline strong{font-weight:700}
.call-pill{position:absolute;left:30px;right:30px;top:970px;background:var(--royal);color:var(--paper);border-radius:24px;padding:10px 18px;font-size:18px;text-transform:uppercase;letter-spacing:1px}
.call-pill b{font-weight:700}
.web{position:absolute;left:0;right:0;top:1030px;text-align:center;color:#d7d9df;font-size:13px;letter-spacing:3px}
/* quote panel */
.quote{position:absolute;top:60px;left:0;right:0;padding:0 34px;text-align:center}
.quote h3{color:var(--royal);font-size:20px;font-weight:800;text-transform:uppercase;margin-bottom:16px}
.phone-row{display:flex;align-items:center;background:var(--royal);border-radius:22px;height:42px;margin-bottom:12px;color:var(--paper);font-weight:700;font-size:21px}
.phone-row .ico{width:42px;height:42px;border-radius:50%;background:var(--paper);border:3px solid var(--royal);display:flex;align-items:center;justify-content:center;flex:none}
.phone-row span{flex:1;text-align:center;padding-right:20px;letter-spacing:1px}
.quote .need{font-size:12px;margin-top:4px}
.quote .need-items{font-size:12px;font-weight:700;text-transform:uppercase;margin-top:4px}
.contact{position:absolute;left:0;right:0;top:780px;text-align:center;color:#e4e6ea}
.contact .brand{font-size:22px;color:var(--sky)}
.icons{display:flex;justify-content:center;gap:12px;margin:16px 0 18px}
.icons span{width:28px;height:28px;border-radius:50%;background:var(--royal);display:flex;align-items:center;justify-content:center}
.contact p{font-size:14px;line-height:1.9}
/* services panel */
.services{position:absolute;top:46px;left:30px;right:24px}
.services .block{margin-bottom:34px}
/* inside */
.banner{position:absolute;top:60px;left:40px;z-index:3;text-transform:uppercase;font-weight:800;color:var(--paper);font-size:34px;line-height:1.08}
.banner .tag{display:inline-block;background:var(--leaf);border-radius:16px;padding:2px 16px;font-size:28px;margin-top:6px}
.in-col{position:absolute;z-index:3;color:var(--paper)}
.in-col .section-kicker{color:var(--royal);font-style:normal;font-weight:700;font-size:19px}
.in-col .section-title{color:var(--paper)}
.in-col .rule{margin:8px 0 14px}
.in-col .list li{font-size:11.5px;line-height:1.3;margin-bottom:5px}
.in-col .list li b{font-weight:700}
.col-residential{top:560px;left:34px;width:340px}
.col-rv{top:580px;left:406px;width:320px}
.circles{position:absolute;top:790px;left:416px;width:300px;height:210px}
.circle{position:absolute;width:108px;height:108px;border-radius:50%;background:var(--royal);border:3px solid #5567d6;color:var(--paper);font-size:11px;font-weight:700;text-transform:uppercase;display:flex;align-items:center;justify-content:center;text-align:center;line-height:1.2}
.callbar{position:absolute;left:0;width:746.66px;bottom:0;height:50px;background:var(--royal);color:var(--paper);font-weight:700;font-size:16px;display:flex;align-items:center;padding-left:34px;text-transform:uppercase;z-index:4}
.facts{position:absolute;top:50px;left:34px;right:28px;color:var(--paper)}
.facts .section-title{font-size:24px}
.facts .rule{background:var(--paper)}
.facts .list li{font-size:12.5px;margin-bottom:10px}
.facts .list li::before{border-color:var(--paper)}
.facts-brand{position:absolute;top:760px;left:0;right:0;font-size:22px;color:var(--paper)}
.facts-brand .dot{background:var(--paper)}
.web-strip{position:absolute;left:0;right:0;bottom:0;height:50px;background:var(--ink);color:var(--paper);font-size:14px;letter-spacing:2px;display:flex;align-items:center;justify-content:center;font-weight:600}
</style>
</head>
<body>

<section class="spread spread--outside">
  <article class="panel" style="background:var(--paper)">
    <div class="services">
      <div class="block">
        <p class="section-kicker">Other</p>
        <h2 class="section-title">Services Offered</h2>
        <div class="rule"></div>
        <ul class="list two-col">
          <li>Agricultural pivot power</li>
          <li>Battery storage systems</li>
          <li>Oil and gas systems</li>
          <li>Off grid designs for cottages / lake houses</li>
          <li>Energy audits</li>
        </ul>
      </div>
      <div class="block">
        <p class="section-kicker">What</p>
        <h2 class="section-title">Makes Us Different</h2>
        <div class="rule"></div>
        <ul class="list two-col">
          <li>In House Engineered Designs</li>
          <li>Design to permit to production service</li>
          <li>Master Electricians</li>
          <li>Repairs or modifications to your existing system</li>
          <li>Energy Market specialists</li>
          <li>Solar Financing options</li>
          <li>Energy consumption reduction evaluations</li>
          <li>Energy Marketing partners</li>
          <li>Professional Electrical Journeymen</li>
        </ul>
      </div>
    </div>
    <div class="photo" role="img" aria-label="Installer in a hard hat fitting a rooftop solar panel" style="top:700px;bottom:0;background:linear-gradient(160deg,#9fb3d6 0%,#5f77b0 45%,#2e3f7c 100%)"></div>
  </article>

  <article class="panel" style="background:var(--paper)">
    <div class="quote">
      <h3>Get a Free Quote</h3>
      <div class="phone-row"><div class="ico"><svg width="18" height="18" viewBox="0 0 24 24"><path d="M6.6 10.8a15 15 0 0 0 6.6 6.6l2.2-2.2c.3-.3.7-.4 1-.2 1.1.4 2.3.6 3.6.6.6 0 1 .4 1 1V20c0 .6-.4 1-1 1A17 17 0 0 1 3 4c0-.6.4-1 1-1h3.5c.6 0 1 .4 1 1 0 1.3.2 2.5.6 3.6.1.3 0 .7-.2 1z" fill="#3446b4"/></svg></div><span>555.201.4400</span></div>
      <div class="phone-row"><div class="ico"><svg width="18" height="18" viewBox="0 0 24 24"><path d="M6.6 10.8a15 15 0 0 0 6.6 6.6l2.2-2.2c.3-.3.7-.4 1-.2 1.1.4 2.3.6 3.6.6.6 0 1 .4 1 1V20c0 .6-.4 1-1 1A17 17 0 0 1 3 4c0-.6.4-1 1-1h3.5c.6 0 1 .4 1 1 0 1.3.2 2.5.6 3.6.1.3 0 .7-.2 1z" fill="#3446b4"/></svg></div><span>555.318.7720</span></div>
      <p class="need">what is needed to get a quote</p>
      <p class="need-items">Address | Power Bill | 10 Minutes</p>
    </div>
    <div class="photo" role="img" aria-label="Solar panel arrays standing on a green grassy field" style="top:300px;height:360px;background:linear-gradient(180deg,#dfe6f2 0%,#b9c7de 40%,#6f9447 70%,#3f6a25 100%)"></div>
    <div class="dark" style="top:560px"></div>
    <svg class="swoosh" style="top:520px" height="140" viewBox="0 0 373 140" preserveAspectRatio="none"><path d="M0 20 C90 40 140 140 373 90 L373 140 L0 140Z" fill="#3446b4"/><path d="M0 60 C100 70 160 150 373 120 L373 140 L0 140Z" fill="#1b1d21"/></svg>
    <div class="contact">
      <div class="brand"><span class="dot"></span>Marigold Works</div>
      <div class="icons">
        <span><svg width="14" height="14" viewBox="0 0 24 24"><rect x="3" y="6" width="18" height="12" rx="1" fill="none" stroke="#fff" stroke-width="2"/><path d="M3 7l9 6 9-6" fill="none" stroke="#fff" stroke-width="2"/></svg></span>
        <span><svg width="14" height="14" viewBox="0 0 24 24"><path d="M12 2a7 7 0 0 0-7 7c0 5 7 13 7 13s7-8 7-13a7 7 0 0 0-7-7zm0 9.5A2.5 2.5 0 1 1 12 6.5a2.5 2.5 0 0 1 0 5z" fill="#fff"/></svg></span>
        <span><svg width="14" height="14" viewBox="0 0 24 24"><circle cx="12" cy="12" r="9" fill="none" stroke="#fff" stroke-width="2"/><path d="M3 12h18M12 3c3 3 3 15 0 18M12 3c-3 3-3 15 0 18" fill="none" stroke="#fff" stroke-width="1.6"/></svg></span>
      </div>
      <p>sales@marigoldworks.com</p>
      <p>Cedar Bend, Alberta, Canada</p>
      <p>www.marigoldworks.com</p>
    </div>
  </article>

  <article class="panel" style="background:var(--paper)">
    <div class="photo" role="img" aria-label="Tilted solar panel array on grass under a soft sky" style="top:0;height:700px;background:linear-gradient(180deg,#ffffff 0%,#e6eaf4 25%,#b6c1dc 50%,#6d8f45 78%,#3e6623 100%)"></div>
    <div class="brand cover-brand"><span class="dot"></span>Marigold Works</div>
    <div class="dark" style="top:660px"></div>
    <svg class="swoosh" style="top:600px" height="140" viewBox="0 0 373 140" preserveAspectRatio="none"><path d="M0 30 C120 50 180 140 373 90 L373 140 L0 140Z" fill="#3446b4"/><path d="M0 70 C120 80 200 150 373 120 L373 140 L0 140Z" fill="#1b1d21"/></svg>
    <h1 class="cover-headline">A Great Place<br>to Start Your<br><span class="green">Renewable</span><br><strong>Energy Project!</strong></h1>
    <div class="call-pill">Call Us <b>555.201.4400</b></div>
    <p class="web">www.marigoldworks.com</p>
  </article>
</section>

<section class="spread spread--inside">
  <article class="panel" style="background:var(--ink);width:746.66px">
    <div class="photo" role="img" aria-label="Close view of blue solar panels on a grassy hill" style="top:0;height:480px;background:linear-gradient(180deg,#2fb3e8 0%,#3d74c4 35%,#26408f 60%,#52803a 85%,#2d4f1c 100%)"></div>
    <svg class="swoosh" style="top:400px;z-index:2" height="140" viewBox="0 0 746 140" preserveAspectRatio="none"><path d="M0 40 C200 20 300 120 746 50 L746 140 L0 140Z" fill="#3446b4"/><path d="M0 80 C220 60 320 150 746 90 L746 140 L0 140Z" fill="#1b1d21"/></svg>
    <div class="banner">Lowest<br>Installed<br>Solar Price<br><span class="tag">Guaranteed</span></div>

    <div class="in-col col-residential">
      <p class="section-kicker">Residential</p>
      <h2 class="section-title">Rooftop PV</h2>
      <div class="rule"></div>
      <ul class="list">
        <li>System sizes from 2.4kW to 12kW</li>
        <li><b>DIY Packages available</b></li>
        <li>Referral Bonus - 250$ for any successful solar referral</li>
        <li><b>Offset some or all of your energy use</b></li>
        <li>Electric Vehicle Charging Systems</li>
        <li><b>Fully insured</b></li>
        <li>25 Year system life</li>
        <li><b>Can raise value of your home by up to $20,000</b></li>
        <li>Extends the life of your roof</li>
        <li><b>100$ donation to a local charity as part of any solar install.</b></li>
        <li>One free solar panel if ordered within one week of your birthday</li>
        <li><b>We offer financing. Finance a solar system with 20% down and you will be saving money immediately.</b></li>
        <li><b>Transfer the loan to your mortgage and increase your savings.</b></li>
        <li>Selling your house and love your solar? We will relocate the system to your new home for a small fee.</li>
      </ul>
    </div>

    <div class="in-col col-rv">
      <h2 class="section-title"><span style="color:var(--royal)">RV</span> Solar</h2>
      <div class="rule"></div>
      <ul class="list">
        <li>DIY 300W package from 500$, 600W package from 700$</li>
        <li><b>Installation services available</b></li>
        <li>Keeps your batteries charged</li>
        <li><b>No longer deal with dead batteries</b></li>
        <li>Become the envy of all campers!</li>
        <li><b>Never have a dead cell phone battery again.</b></li>
      </ul>
    </div>
    <div class="circles">
      <div class="circle" style="left:0;top:0">RV<br>Packages</div>
      <div class="circle" style="left:130px;top:-14px">Residential<br>Packages</div>
      <div class="circle" style="left:40px;top:96px">Commercial<br>Packages</div>
      <div class="circle" style="left:170px;top:84px">Energy<br>Audit</div>
    </div>
    <div class="callbar">Call Us Today! 555.201.4400 or 555.318.7720</div>
  </article>

  <article class="panel" style="background:linear-gradient(180deg,var(--royal) 0%,#2f5fc8 100%)">
    <div class="facts">
      <h2 class="section-title">Some Facts<br>on Solar</h2>
      <div class="rule"></div>
      <ul class="list">
        <li>Alberta is the sunniest province in Canada and comparable to Florida</li>
        <li>Systems are designed to last 25 years but operate for as long as 40 years</li>
        <li>Virtually no maintenance required!</li>
        <li>How your power bill works.</li>
        <li>Protect yourself from rising power costs</li>
        <li>Not everyone can have solar. Once 30-40% of the market has solar, utilities will not allow all solar systems to be installed.</li>
        <li>Dispel the snow myth: Snow only reduces a system's output by 5-8% over the course of a year. This is because our sunny hours are mostly made up in the longer summer days.</li>
        <li>Solar panels are nearly indestructible. Hail cannot damage a solar panel.</li>
        <li>Any extra power generated in the summer is sold back to the grid as a credit on your bill.</li>
      </ul>
    </div>
    <div class="brand facts-brand"><span class="dot"></span>Marigold Works</div>
    <div class="photo" role="img" aria-label="Installer in a hard hat working on rooftop solar panels with a drill" style="top:820px;bottom:50px;background:linear-gradient(160deg,#3b6ed0 0%,#2b4b9c 55%,#1e2c5e 100%)"></div>
    <div class="web-strip">www.marigoldworks.com</div>
  </article>
</section>

</body>
</html>
```